New Business Card Design Project

Make a kick ass business card for The Otter Tea Mug, using the designs. I also might like the 2nd place design logo on the back? Maybe all black with that? Not sure. Also, I'm cool with it being on metal, plastic, glass? or whatever for the business card. Maybe shaped like a shark? Let me know what else you need? Would like designs in the next day or so. Thank you.
Target Market(s)
Anyone that is cool
Contact Information for Business Card
Name: Dorian Fenwick
Phone: 317.594.8126
inventor/creator/entrepreneur/owner
www.theottertyeamug.example
social media links
https://www.facebook.com/theottertyeamug
https://twitter.com/otter_brew
https://www.instagram.com/theottertyeamug/
I'll get the Pinterest one soon
Colors
Designer to choose colors to be used in the design.
Requirements
Must have
- The Otter Tea Mug
- www.theottertyeamug.example
- social media tags?
- My logos and picture/photo of wine glass
Nice to have
- Maybe shaped like a wine glass or shark
- I'll let you decide but my same colors from my website would be nice

```html
<!DOCTYPE html>
<html lang="en">
<head>
<meta charset="utf-8">
<title>The Otter Tea Mug – Business Card</title>
<link href="https://fonts.googleapis.com/css2?family=Quicksand:wght@400&family=Open+Sans:wght@400;700&display=swap" rel="stylesheet">
<style>
  :root {
    --backdrop: #2b2b2d;
    --card-red: #b9434a;
    --card-black: #1c1c1e;
    --accent-red: #c8323c;
    --light: #ffffff;
    --glass-grey: #d4d4d4;
    --muted: #e6e6e6;
  }
  * { box-sizing: border-box; margin: 0; padding: 0; }
  html, body {
    width: 1200px; height: 900px; overflow: hidden;
    background: var(--backdrop);
  }
  .canvas { position: relative; width: 1200px; height: 900px; }

  .card {
    position: absolute;
    width: 640px; height: 366px;
    box-shadow: 0 14px 30px rgba(0,0,0,.45);
    overflow: hidden;
  }

  /* Front */
  .card-front { left: 60px; top: 60px; background: var(--card-red); }
  .glass-art {
    position: absolute; left: 70px; top: 0;
    width: 200px; height: 366px;
    background: linear-gradient(180deg, rgba(212,212,212,.35), rgba(212,212,212,.12));
  }
  .front-wordmark {
    position: absolute; right: 58px; top: 236px;
    font-family: 'Quicksand', sans-serif; font-weight: 400;
    font-size: 38px; letter-spacing: .5px;
    color: var(--light);
  }

  /* Back */
  .card-back { left: 500px; top: 474px; background: var(--card-black); }
  .back-wordmark {
    position: absolute; left: 44px; top: 190px;
    font-family: 'Quicksand', sans-serif; font-weight: 400;
    font-size: 38px; letter-spacing: .5px;
    color: var(--light);
  }
  .divider {
    position: absolute; left: 372px; top: 92px;
    width: 1.5px; height: 170px;
    background: var(--muted);
  }
  .contact {
    position: absolute; left: 392px; top: 92px;
    font-family: 'Open Sans', sans-serif; color: var(--light);
  }
  .contact-name {
    font-weight: 700; font-size: 20px; color: var(--accent-red); line-height: 1.1;
  }
  .contact-role { font-size: 10.5px; margin: 3px 0 12px; white-space: nowrap; }
  .contact-list { list-style: none; }
  .contact-list li {
    display: flex; align-items: center; gap: 8px;
    font-size: 13px; line-height: 21px; white-space: nowrap;
  }
  .contact-list svg { width: 12px; height: 12px; flex: none; }
</style>
</head>
<body>
<main class="canvas">

  <section class="card card-front" aria-label="Card front">
    <div class="glass-art" role="img" aria-label="Outline of a wine glass with the brand mark inside the bowl"></div>
    <div class="front-wordmark">OtterTeaMug</div>
  </section>

  <section class="card card-back" aria-label="Card back">
    <div class="back-wordmark">OtterTeaMug</div>
    <div class="divider"></div>
    <div class="contact">
      <p class="contact-name">Dorian Fenwick</p>
      <p class="contact-role">Inventor | Creator | Entrepreneur | Owner</p>
      <ul class="contact-list">
        <li>
          <svg viewBox="0 0 12 12" aria-hidden="true"><path d="M2.5 1h2l1 3-1.3 1a6.5 6.5 0 0 0 2.8 2.8L8 6.5l3 1v2A1.5 1.5 0 0 1 9.5 11 8.5 8.5 0 0 1 1 2.5 1.5 1.5 0 0 1 2.5 1z" fill="#c8323c"/></svg>
          317.594.8126
        </li>
        <li>
          <svg viewBox="0 0 12 12" aria-hidden="true"><circle cx="6" cy="6" r="5" fill="none" stroke="#c8323c" stroke-width="1.4"/><path d="M1 6h10M6 1c2.2 2.6 2.2 7.4 0 10M6 1c-2.2 2.6-2.2 7.4 0 10" fill="none" stroke="#c8323c" stroke-width="1"/></svg>
          www.theottertyeamug.example
        </li>
        <li>
          <svg viewBox="0 0 12 12" aria-hidden="true"><circle cx="6" cy="6" r="5.5" fill="#c8323c"/></svg>
          theottertyeamug
        </li>
        <li>
          <svg viewBox="0 0 12 12" aria-hidden="true"><circle cx="6" cy="6" r="5.5" fill="#c8323c"/></svg>
          otter_brew
        </li>
        <li>
          <svg viewBox="0 0 12 12" aria-hidden="true"><circle cx="6" cy="6" r="5.5" fill="#c8323c"/></svg>
          theottertyeamug
        </li>
      </ul>
    </div>
  </section>

</main>
</body>
</html>
```